Best in class business looking for best in class stationery that accurately reflects the brand image we are trying to build as the brand expands throughout the country. The Varying items should be an eye catching design that makes even the simplest letter or small business card stand out in the crowd.

Target Market(s)

Professionals

Industry/Entity Type

Real Estate

Other font styles liked:
• See atttached logo

Requirements
Must have
• Letterhead
• Business cards
• Envelopes
• Labels for larger mailings
Nice to have
• Folders
• Notebook
Should not have
• Stale design elements

```html
<!DOCTYPE html>
<html lang="en">
<head>
<meta charset="utf-8">
<title>Ardent Property Group — Stationery</title>
<link href="https://fonts.googleapis.com/css2?family=Open+Sans:wght@400;600&display=swap" rel="stylesheet">
<style>
  :root {
    --navy: #283575;
    --brand-blue: #2b7fc1;
    --ink: #3a3a3a;
    --muted: #7a7a7a;
    --rule: #9a9a9a;
    --paper: #ffffff;
    --backdrop: #e7e8ea;
    --mark-grey: #c4c6c9;
  }
  * { margin: 0; padding: 0; box-sizing: border-box; }
  html, body { width: 1200px; height: 1041px; overflow: hidden; }
  body {
    position: relative;
    background: var(--backdrop);
    font-family: "Open Sans", Arial, sans-serif;
    color: var(--ink);
  }
  .sheet { position: absolute; background: var(--paper); }

  .brand {
    display: flex; align-items: center; gap: 6px;
    font-family: "Open Sans", Arial, sans-serif;
    font-weight: 600; text-transform: uppercase;
    letter-spacing: 0.06em; color: var(--navy); white-space: nowrap;
  }
  .brand-square { display: inline-block; background: currentColor; }

  /* Letterhead */
  .letterhead { left: 81px; top: 62px; width: 455px; height: 641px; }
  .letterhead .brand { position: absolute; left: 56px; top: 44px; font-size: 11px; }
  .letterhead .brand-square { width: 10px; height: 10px; }
  .letterhead-address {
    position: absolute; right: 22px; top: 44px;
    font-size: 9px; line-height: 14px; color: var(--muted); letter-spacing: 0.04em;
  }
  .letterhead-rule { position: absolute; left: 56px; right: 22px; top: 100px; border-top: 1px solid var(--rule); }
  .letter {
    position: absolute; left: 60px; top: 137px; width: 325px;
    font-size: 8.4px; line-height: 12.4px; color: var(--ink);
  }
  .letter .recipient { margin-bottom: 21px; }
  .letter p { text-align: justify; }
  .letter .greeting { margin-bottom: 3px; }
  .letter .signoff { margin-top: 0; }
  .letter .signature { margin-top: 14px; }

  /* Folder */
  .folder { left: 670px; top: 59px; width: 455px; height: 645px; background: var(--navy); }
  .folder .brand {
    position: absolute; left: 0; right: 0; top: 365px; justify-content: center;
    color: var(--brand-blue); font-size: 25px; gap: 12px;
  }
  .folder .brand-square { width: 22px; height: 22px; }

  /* Business cards */
  .card-back { left: 323px; top: 751px; width: 288px; height: 166px; background: var(--navy); }
  .card-back .brand {
    position: absolute; left: 70px; top: 88px; color: var(--brand-blue); font-size: 11px;
  }
  .card-back .brand-square { width: 10px; height: 10px; }

  .card-front { left: 85px; top: 810px; width: 290px; height: 171px; box-shadow: 0 1px 4px rgba(0,0,0,0.15); }
  .card-front .brand { position: absolute; left: 14px; top: 46px; font-size: 9px; gap: 5px; }
  .card-front .brand-square { width: 8px; height: 8px; }
  .card-person { position: absolute; right: 18px; top: 72px; text-align: right; }
  .card-name { font-size: 10.5px; font-weight: 600; color: var(--navy); letter-spacing: 0.05em; }
  .card-title { font-size: 6px; color: var(--muted); letter-spacing: 0.08em; text-transform: uppercase; margin-top: 2px; }
  .card-phones { position: absolute; left: 14px; top: 121px; font-size: 7.5px; line-height: 13px; color: var(--muted); }
  .card-links { position: absolute; right: 14px; top: 121px; font-size: 7.5px; line-height: 13px; color: var(--muted); text-align: right; }
  .contact-row { display: flex; align-items: center; gap: 5px; }
  .card-links .contact-row { justify-content: flex-end; }
  .contact-row svg { width: 7px; height: 7px; fill: var(--navy); flex: none; }

  /* Envelope */
  .envelope { left: 648px; top: 748px; width: 519px; height: 233px; overflow: hidden; }
  .envelope-flap { position: absolute; left: 0; top: 0; width: 519px; height: 46px; }
  .envelope .brand-small { position: absolute; left: 30px; top: 63px; font-size: 9px; gap: 5px; }
  .envelope .brand-small .brand-square { width: 8px; height: 8px; }
  .envelope .brand-large { position: absolute; left: 276px; top: 145px; font-size: 15px; color: var(--mark-grey); gap: 8px; }
  .envelope .brand-large .brand-square { width: 14px; height: 14px; }
  .envelope-address { position: absolute; left: 28px; top: 180px; font-size: 10px; line-height: 15px; color: var(--muted); letter-spacing: 0.05em; }
</style>
</head>
<body>

  <!-- Letterhead -->
  <section class="sheet letterhead">
    <div class="brand"><span class="brand-square"></span>Ardent Property Group</div>
    <div class="letterhead-address">
      City, State Name,<br>14 Harbor Lane<br>(555) 010-2200
    </div>
    <div class="letterhead-rule"></div>
    <article class="letter">
      <div class="recipient">
        Mara Lindqvist<br>Title<br>Company Name<br>208 Cedar Avenue<br>Millbrook, State ZIP<br>Date 1/30/12
      </div>
      <p class="greeting">Dear Mara,</p>
      <p>Thank you for considering our firm for the management of your residential and commercial holdings. Our team has reviewed the portfolio you shared and prepared an outline of services, timelines and reporting that fits the goals we discussed during our meeting last week.</p>
      <p>We propose a phased onboarding that begins with a full property inspection, followed by tenant communication, vendor review and a clear monthly statement. Each building will have a dedicated manager and a single point of contact for urgent repairs. Our leasing staff will market vacant units across regional listings and screen applicants with care. We also provide quarterly reviews so that rent levels, maintenance budgets and capital plans stay aligned with your expectations. Please let us know a convenient time to walk through the proposal in person.</p>
      <p class="signoff">Sincerely yours,</p>
      <p class="signature">Name Here</p>
    </article>
  </section>

  <!-- Folder -->
  <section class="sheet folder">
    <div class="brand"><span class="brand-square"></span>Ardent Property Group</div>
  </section>

  <!-- Business card, back -->
  <section class="sheet card-back">
    <div class="brand"><span class="brand-square"></span>Ardent Property Group</div>
  </section>

  <!-- Business card, front -->
  <section class="sheet card-front">
    <div class="brand"><span class="brand-square"></span>Ardent Property Group</div>
    <div class="card-person">
      <div class="card-name">NOEL VARGA</div>
      <div class="card-title">Managing Director</div>
    </div>
    <div class="card-phones">
      <div class="contact-row"><svg viewBox="0 0 10 10"><path d="M2 0h2l1 3-1.5 1a6 6 0 0 0 2.5 2.5L7 5l3 1v2a2 2 0 0 1-2 2A8 8 0 0 1 0 2a2 2 0 0 1 2-2z"/></svg>(555) 010-2200</div>
      <div class="contact-row"><svg viewBox="0 0 10 10"><rect x="2" y="0" width="6" height="10" rx="1"/></svg>(555) 010-2211</div>
      <div class="contact-row"><svg viewBox="0 0 10 10"><path d="M1 10V3h8v7zM2 0h6v2H2z"/></svg>(555) 010-2233</div>
    </div>
    <div class="card-links">
      <div class="contact-row">hello@ardentpg.co<svg viewBox="0 0 10 10"><path d="M0 2h10v6H0z"/></svg></div>
      <div class="contact-row">www.ardentpg.co<svg viewBox="0 0 10 10"><circle cx="5" cy="5" r="5"/></svg></div>
      <div class="contact-row">City, State Name, 14 Harbor Lane<svg viewBox="0 0 10 10"><path d="M5 0a3.5 3.5 0 0 1 3.5 3.5C8.5 6 5 10 5 10S1.5 6 1.5 3.5A3.5 3.5 0 0 1 5 0z"/></svg></div>
    </div>
  </section>

  <!-- Envelope -->
  <section class="sheet envelope">
    <svg class="envelope-flap" viewBox="0 0 519 46" preserveAspectRatio="none">
      <polygon points="0,34 32,0 519,0 519,46" fill="var(--navy)"/>
    </svg>
    <div class="brand brand-small"><span class="brand-square"></span>Ardent Property Group</div>
    <div class="brand brand-large"><span class="brand-square"></span>Ardent Property Group</div>
    <div class="envelope-address">City, State Name,<br>14 Harbor Lane</div>
  </section>

</body>
</html>
```